Copperfork Roundtable Podcast

We need a Podcast Cover design that is compatible with Apple Podcasts, Spotify, etc. In this podcast, we interview the real movers & shakers in the foodservice industry who cut through the noise to get to the top.

```html
<!DOCTYPE html>
<html lang="en">
<head>
<meta charset="utf-8">
<title>Copperfork Roundtable Podcast – Cover</title>
<link rel="stylesheet" href="https://fonts.googleapis.com/css2?family=Bebas+Neue&family=Montserrat:ital,wght@1,800&display=swap">
<style>
  :root {
    --stage: #d9d9d9;
    --cover-black: #070707;
    --brand-orange: #f7931e;
    --orange-deep: #e07f12;
    --suit-navy: #1b2b45;
    --ink-white: #ffffff;
  }
  html, body {
    margin: 0;
    padding: 0;
    width: 1200px;
    height: 807px;
    overflow: hidden;
    background: var(--stage);
  }
  .canvas {
    position: relative;
    width: 1200px;
    height: 807px;
  }
  .podcast-cover {
    position: absolute;
    left: 220px;
    top: 23px;
    width: 760px;
    height: 760px;
    display: block;
  }
  .cover-title-top { font-family: "Bebas Neue", "Oswald", sans-serif; fill: var(--ink-white); }
  .cover-title-main { font-family: "Bebas Neue", "Oswald", sans-serif; fill: var(--brand-orange); }
  .cover-kicker { font-family: "Montserrat", "Arial", sans-serif; font-weight: 800; font-style: italic; fill: var(--ink-white); }
  .frame-line { stroke: var(--ink-white); stroke-width: 2; fill: none; }
  .accent-dot { fill: var(--brand-orange); }
</style>
</head>
<body>
<main class="canvas">
  <svg class="podcast-cover" viewBox="0 0 760 760" xmlns="http://www.w3.org/2000/svg">
    <defs>
      <linearGradient id="host-photo-tone" x1="0" y1="0" x2="0" y2="1">
        <stop offset="0" stop-color="var(--brand-orange)"/>
        <stop offset="0.5" stop-color="var(--orange-deep)"/>
        <stop offset="0.62" stop-color="var(--suit-navy)"/>
        <stop offset="1" stop-color="#0b111c"/>
      </linearGradient>
    </defs>

    <rect class="cover-background" width="760" height="760" fill="var(--cover-black)"/>

    <g class="host-photo" role="img" aria-label="Portrait photo of the podcast host in a navy blazer against an orange brush splash">
      <path d="M560 0 L760 0 L760 760 L420 760 L430 600 L470 540 L440 470 L480 400 L430 330 L480 280 L500 220 L540 200 L560 140 L580 100 L570 50 Z" fill="url(#host-photo-tone)"/>
    </g>

    <g class="host-signature" role="img" aria-label="Handwritten signature of host Dane Arvello">
      <rect x="43" y="243" width="259" height="191" fill="#141414" opacity="0.6"/>
    </g>

    <path class="frame-line frame-top-left" d="M41 164 V36 H117"/>
    <circle class="accent-dot" cx="41" cy="179" r="4.6"/>
    <circle class="accent-dot" cx="41" cy="195" r="4.6"/>
    <circle class="accent-dot" cx="41" cy="212" r="4.6"/>

    <path class="frame-line frame-bottom-right" d="M723 601 V726 H647"/>
    <circle class="accent-dot" cx="721" cy="549" r="4.6"/>
    <circle class="accent-dot" cx="721" cy="565" r="4.6"/>
    <circle class="accent-dot" cx="721" cy="581" r="4.6"/>

    <text class="cover-title-top" x="43" y="549" font-size="126" textLength="490" lengthAdjust="spacingAndGlyphs">COPPERFORK</text>
    <text class="cover-title-main" x="43" y="657" font-size="136" textLength="588" lengthAdjust="spacingAndGlyphs">ROUNDTABLE</text>
    <text class="cover-kicker" x="368" y="688" font-size="26" textLength="253" lengthAdjust="spacing">PODCAST</text>
  </svg>
</main>
</body>
</html>
```